Kit com 6 Layouts de Post para Redes Sociais (Facebook, Instagram e etc) + Capa de Facebookpara RZ SEGUROS E CONSORCIOS
Postado por: gestao.rzseguros_2840395726   Estou Offline

```html
<!DOCTYPE html>
<html lang="pt-BR">
<head>
<meta charset="UTF-8">
<title>RZ Seguros – Seguro de Vida</title>
<link href="https://fonts.googleapis.com/css2?family=Poppins:wght@300;400;500;600&display=swap" rel="stylesheet">
<style>
  :root {
    --page: #ffffff;
    --bg-top: #f5eefa;
    --bg-bottom: #ece1f3;
    --band: rgba(215, 188, 233, 0.5);
    --purple-light: #b57cd0;
    --purple: #9a48b9;
    --purple-deep: #5e2a86;
    --ink: #33244a;
    --ink-soft: #4f3f66;
    --hair: #5a3f35;
    --skin: #e7b9a4;
    --shirt-pink: #e8c6cf;
    --shirt-white: #f6f1f4;
  }
  * { margin: 0; padding: 0; box-sizing: border-box; }
  html, body { width: 1200px; height: 1200px; overflow: hidden; }
  body { font-family: "Poppins", sans-serif; background: var(--page); }

  .post {
    position: absolute;
    left: 120px;
    top: 0;
    width: 960px;
    height: 1200px;
    overflow: hidden;
    background: linear-gradient(180deg, var(--bg-top) 0%, var(--bg-bottom) 100%);
  }

  .deco-band {
    position: absolute;
    left: -40px;
    top: 440px;
    width: 1040px;
    height: 72px;
    background: var(--band);
    transform: skewY(-2deg);
  }

  .brand {
    position: absolute;
    left: 60px;
    top: 170px;
    display: flex;
    align-items: center;
    gap: 14px;
  }
  .brand-dot {
    width: 26px;
    height: 26px;
    border-radius: 50%;
    background: var(--purple);
  }
  .brand-name {
    font-size: 54px;
    font-weight: 500;
    color: var(--purple-deep);
    letter-spacing: -1px;
    line-height: 1;
  }

  .headline {
    position: absolute;
    right: 58px;
    top: 210px;
    text-align: right;
    line-height: 1;
  }
  .headline-light {
    display: block;
    font-size: 58px;
    font-weight: 300;
    color: var(--purple-light);
  }
  .headline-strong {
    display: block;
    margin-top: 4px;
    font-size: 58px;
    font-weight: 600;
    color: var(--purple);
  }

  .tagline {
    position: absolute;
    right: 58px;
    top: 352px;
    text-align: right;
    color: var(--ink);
    line-height: 1.12;
  }
  .tagline-main { display: block; font-size: 40px; font-weight: 500; }
  .tagline-sub { display: block; font-size: 40px; font-weight: 300; }

  .contact {
    position: absolute;
    right: 58px;
    top: 484px;
    display: flex;
    align-items: center;
    gap: 12px;
  }
  .contact-icon { width: 76px; height: 76px; }
  .contact-text { color: var(--ink-soft); line-height: 1.15; }
  .contact-cta { display: block; font-size: 23px; font-weight: 400; }
  .contact-phone { display: block; font-size: 33px; font-weight: 500; color: var(--ink); }

  .family-photo {
    position: absolute;
    left: 0;
    top: 560px;
    width: 960px;
    height: 640px;
    border-radius: 120px 120px 0 0;
    background:
      linear-gradient(180deg, rgba(90,63,53,0.85) 0%, rgba(90,63,53,0.55) 22%, rgba(231,185,164,0.9) 40%, rgba(231,185,164,0.6) 62%, rgba(0,0,0,0) 75%),
      linear-gradient(90deg, var(--shirt-pink) 0%, var(--shirt-pink) 34%, var(--shirt-white) 42%, var(--shirt-white) 100%);
  }
</style>
</head>
<body>
  <main class="post">
    <div class="deco-band"></div>

    <div class="brand">
      <span class="brand-dot"></span>
      <span class="brand-name">RZ Seguros</span>
    </div>

    <h1 class="headline">
      <span class="headline-light">SEGURO</span>
      <span class="headline-strong">DE VIDA</span>
    </h1>

    <p class="tagline">
      <span class="tagline-main">seu bem mais precioso</span>
      <span class="tagline-sub">merece segurança!</span>
    </p>

    <div class="contact">
      <svg class="contact-icon" viewBox="0 0 76 76" aria-hidden="true">
        <circle cx="38" cy="38" r="33" fill="none" stroke="var(--purple)" stroke-width="4"/>
        <path d="M28 24 L33 23 L36 31 L32 34 Q36 42 43 45 L46 41 L54 44 L53 49 Q50 54 44 52 Q30 47 24 33 Q23 27 28 24 Z" fill="var(--purple)"/>
      </svg>
      <p class="contact-text">
        <span class="contact-cta">Faça AGORA uma cotação</span>
        <span class="contact-phone">+ 55 (35) 9712-3408</span>
      </p>
    </div>

    <div class="family-photo" role="img" aria-label="Fotografia de uma família sorridente: pai de camisa rosa, filha e mãe de blusa branca"></div>
  </main>
</body>
</html>
```